I need three graphics made that will go on walls in a basketball lockerroom

I need three graphics made that will go on a basketball lockerroom wall. Here are the specifics.
Graphic 1 (Size 115" wide by 52" tall, min 150 DPI)
This should be something that displays the acronym for TOLVAR. The main background color should be the teal color attached. Use logos and the other approved colors as needed.
Standards
Intensity
Effort
Grit
Energy
Love
Graphic 2 (Size 88" wide by 52" tall, min 150 DPI)
This one should be on the Navy Blue background color attached
and impactful way say Attitude and Effort
Graphic 3 (Size 100" wide by 18" tall, min 150 DPI)
This goes along the top of the way and needs to say
(THS logo) Stars Lead the Way (Star logo) Tolvar Basketball (THS logo)
All three of these need to feel like they are of the same style. For Graphic #2 I thought something maybe like the attached basketball except use the S Star in the middle and say attitude and effort using the colors .. but I'm open to other ideas

```html
<!DOCTYPE html>
<html lang="en">
<head>
<meta charset="utf-8">
<title>Tolvar Basketball Locker Room Graphics</title>
<link rel="stylesheet" href="https://fonts.googleapis.com/css2?family=Alfa+Slab+One&family=Graduate&family=Oswald:wght@700&display=swap">
<style>
  :root {
    --page: #f5f5f5;
    --label: #4a4a4a;
    --teal-deep: #07474f;
    --teal: #0f6e72;
    --teal-bright: #1fb3bc;
    --navy-deep: #0a1f63;
    --navy: #13319a;
    --silver: #dcdcdc;
    --outline: #1c2760;
    --white: #ffffff;
    --slash: #0b1a2e;
  }
  * { box-sizing: border-box; margin: 0; padding: 0; }
  html, body { width: 779px; height: 1200px; overflow: hidden; background: var(--page); }
  .sheet { position: relative; width: 779px; height: 1200px; }

  .panel { position: absolute; overflow: hidden; box-shadow: 6px 12px 14px rgba(0,0,0,.35); }
  .panel-photo { position: absolute; inset: 0; }
  .panel-slashes { position: absolute; inset: 0; width: 100%; height: 100%; }
  .panel-label {
    position: absolute; left: 0; width: 779px; text-align: center;
    font-family: "Alfa Slab One", "Oswald", sans-serif; font-size: 44px;
    color: var(--label); letter-spacing: 1px; line-height: 1;
  }

  .team-name {
    position: absolute; font-family: "Graduate", serif; color: var(--silver);
    line-height: 1; white-space: nowrap; transform: translate(-50%, -50%);
  }
  .star-mark {
    position: absolute; border-radius: 50%; transform: translate(-50%, -50%);
    background: var(--teal-bright); border: 2px solid var(--white);
  }

  /* Graphic 1 */
  .values-board { left: 105px; top: 132px; width: 570px; height: 257px; }
  .values-board .panel-photo { background: radial-gradient(ellipse at 45% 40%, #138089 0%, var(--teal) 45%, var(--teal-deep) 100%); }
  .rule-lines { position: absolute; top: 48px; width: 57px; }
  .rule-lines span { display: block; height: 1px; background: rgba(255,255,255,.7); margin-bottom: 5px; }
  .rule-lines-left { left: 105px; }
  .rule-lines-left span:nth-child(2) { margin-left: 12px; }
  .rule-lines-left span:nth-child(3) { margin-left: 24px; }
  .rule-lines-right { left: 391px; }
  .rule-lines-right span:nth-child(2) { width: 45px; }
  .rule-lines-right span:nth-child(3) { width: 33px; }
  .acronym-letter {
    position: absolute; top: 100px; transform: translateX(-50%);
    font-family: "Graduate", serif; font-size: 104px; line-height: 1; color: var(--silver);
    -webkit-text-stroke: 3px var(--outline); paint-order: stroke fill;
    text-shadow: 2px 3px 0 var(--outline);
  }
  .value-word {
    position: absolute; top: 203px; transform: translateX(-50%);
    font-family: "Graduate", serif; font-size: 12px; font-weight: 700; color: var(--white); white-space: nowrap;
  }
  .divider-dot {
    position: absolute; top: 148px; width: 9px; height: 9px; border-radius: 50%;
    transform: translate(-50%, -50%); background: var(--teal-bright); border: 1px solid var(--white);
  }

  /* Graphic 2 */
  .attitude-board { left: 140px; top: 507px; width: 500px; height: 296px; }
  .attitude-board .panel-photo { background: linear-gradient(120deg, #0c2a85 0%, var(--navy) 50%, var(--navy-deep) 100%); }
  .slogan-line {
    position: absolute; left: 0; width: 100%; text-align: center;
    font-family: "Alfa Slab One", serif; color: var(--white); line-height: 1;
  }
  .slogan-attitude { top: 36px; font-size: 78px; letter-spacing: -1px; }
  .slogan-amp { top: 116px; font-size: 58px; }
  .slogan-effort { top: 180px; font-size: 78px; letter-spacing: -1px; left: -5px; }

  /* Graphic 3 */
  .header-band { left: 105px; top: 933px; width: 570px; height: 102px; }
  .header-band .panel-photo { background: linear-gradient(100deg, var(--navy-deep) 0%, var(--navy) 60%, #1a4aa8 100%); }
  .band-text {
    position: absolute; transform: translateX(-50%); text-align: center;
    font-family: "Graduate", serif; font-size: 19px; font-weight: 700; line-height: 23px;
    color: var(--white); white-space: nowrap; top: 28px;
  }
  .band-text .accent { color: var(--teal-bright); }
</style>
</head>
<body>
<main class="sheet">

  <section class="panel values-board">
    <div class="panel-photo" role="img" aria-label="Teal-tinted photo of basketball players and a packed crowd"></div>
    <svg class="panel-slashes" viewBox="0 0 570 257" preserveAspectRatio="none" aria-hidden="true">
      <polygon points="430,0 570,0 570,40" fill="var(--slash)" opacity=".75"/>
      <polygon points="500,0 570,0 570,80" fill="#9aa3a8" opacity=".5"/>
      <polygon points="0,160 0,257 120,257" fill="var(--slash)" opacity=".75"/>
      <polygon points="0,200 0,257 60,257" fill="#9aa3a8" opacity=".6"/>
    </svg>
    <div class="rule-lines rule-lines-left"><span></span><span></span><span></span></div>
    <div class="rule-lines rule-lines-right"><span></span><span></span><span></span></div>
    <div class="star-mark" style="left:196px;top:57px;width:22px;height:22px"></div>
    <div class="team-name" style="left:279px;top:56px;font-size:34px">THS</div>
    <div class="star-mark" style="left:361px;top:57px;width:22px;height:22px"></div>

    <div class="acronym-letter" style="left:63px">T</div>
    <div class="divider-dot" style="left:113px"></div>
    <div class="acronym-letter" style="left:159px">O</div>
    <div class="divider-dot" style="left:205px"></div>
    <div class="acronym-letter" style="left:247px">L</div>
    <div class="divider-dot" style="left:290px"></div>
    <div class="acronym-letter" style="left:333px">V</div>
    <div class="divider-dot" style="left:376px"></div>
    <div class="acronym-letter" style="left:416px">A</div>
    <div class="divider-dot" style="left:457px"></div>
    <div class="acronym-letter" style="left:499px">R</div>

    <div class="value-word" style="left:64px">STANDARDS</div>
    <div class="value-word" style="left:159px">INTENSITY</div>
    <div class="value-word" style="left:247px">EFFORT</div>
    <div class="value-word" style="left:333px">GRIT</div>
    <div class="value-word" style="left:416px">ENERGY</div>
    <div class="value-word" style="left:499px">LOVE</div>
  </section>
  <h2 class="panel-label" style="top:434px">GRAPHIC 1</h2>

  <section class="panel attitude-board">
    <div class="panel-photo" role="img" aria-label="Navy-tinted photo of a player shooting in front of an arena crowd"></div>
    <svg class="panel-slashes" viewBox="0 0 500 296" preserveAspectRatio="none" aria-hidden="true">
      <polygon points="0,200 0,296 140,296" fill="var(--slash)" opacity=".7"/>
      <polygon points="0,240 0,296 70,296" fill="#9aa3a8" opacity=".5"/>
    </svg>
    <div class="slogan-line slogan-attitude">ATTITUDE</div>
    <div class="star-mark" style="left:177px;top:147px;width:26px;height:26px"></div>
    <div class="slogan-line slogan-amp">&amp;</div>
    <div class="star-mark" style="left:322px;top:147px;width:26px;height:26px"></div>
    <div class="slogan-line slogan-effort">EFFORT</div>
  </section>
  <h2 class="panel-label" style="top:831px">GRAPHIC 2</h2>

  <section class="panel header-band">
    <div class="panel-photo" role="img" aria-label="Navy and blue brushed texture background"></div>
    <svg class="panel-slashes" viewBox="0 0 570 102" preserveAspectRatio="none" aria-hidden="true">
      <polygon points="0,50 0,102 60,102" fill="var(--slash)" opacity=".7"/>
      <polygon points="570,70 570,102 520,102" fill="#9aa3a8" opacity=".6"/>
    </svg>
    <div class="team-name" style="left:66px;top:51px;font-size:30px">THS</div>
    <div class="band-text" style="left:184px">STARS <span class="accent">LEAD</span><br>THE WAY</div>
    <div class="star-mark" style="left:280px;top:51px;width:24px;height:24px"></div>
    <div class="band-text" style="left:382px">TOLVAR<br><span class="accent">BASKETBALL</span></div>
    <div class="team-name" style="left:505px;top:51px;font-size:30px">THS</div>
  </section>
  <h2 class="panel-label" style="top:1079px">GRAPHIC 3</h2>

</main>
</body>
</html>
```